bargainmentor.net - Podcast Guest Marketing E-Flyer PDF

Dear Designers:I am in need of an attractive and attention-getting layout and design for a three-page marketing flyer (commonly known as a media one sheet) that will be sent via e-mail, as PDF file, to various Podcast hosts to market me as a guest on their podcasts. I want the design of the document to "mirror" the design and branding on my parent bargainmentor.net website. I am providing ALL the edited and proofread copy and content - the designer just needs to create the design for this marketing document. I want an active PDF document and icons should be used for ProLink, Phone, E-mail , and website- with hyperlinks that connect accordingly. I need a fast turnaround.
Updates

Dear Designers - instead of using the photo in the project file of me speaking to the audience for the banner image - I thought it would be a better idea to make this marketing piece specific to Podcast Hosts. Therefore, an image such as the one in the link below would be good to use for a banner image. https://www.pixtrove-example.net/gallery?topic=recording+booth+images&ref=qz7&view=grid&id=Kx93LmPwa2RtVbN8YcQdE4&w=1377&h=804#pic=vRmalqobet:

Target Market(s)

This PDF document will be sent to 650 Podcast hosts in North America via a broadcast e-mail.

Font styles to use
Sans Serif

Colors
ec1f27
ffffff
000000
333333
9d9d9d

Requirements
Must have
• A three-page layout that is easy to navigate in PDF form.
• Proper font styles and sizes for key emphasis areas on the document/
• Consistent branding to mirror my bargainmentor.net parent website
• Must be easy for people to read
• Attention-getting design elements and layout
• Professional and sophisticated design
• Icons for contact information
Should not have
• Should not be cluttered and junky-looking.
• Should not use small font sizes that makes it difficult to read.
• If Podcast hosts are interested in having me as a guest - they will read the content as required on three-pages

```html
<!DOCTYPE html>
<html lang="en">
<head>
<meta charset="utf-8">
<title>bargainmentor.net – Podcast Guest One Sheet</title>
<link href="https://fonts.googleapis.com/css2?family=Lato:wght@300;400;700;900&display=swap" rel="stylesheet">
<style>
:root{
  --red:#ec1f27;
  --white:#ffffff;
  --black:#000000;
  --ink:#333333;
  --grey:#9d9d9d;
  --stage:#e4e6e7;
  --paper-tint:#f3f3f4;
  --band:#141414;
}
*{box-sizing:border-box;margin:0;padding:0}
html,body{width:1200px;height:634px;overflow:hidden}
body{background:var(--stage);font-family:"Lato",Arial,sans-serif;color:var(--ink);position:relative}
.page{position:absolute;top:64px;width:371px;height:522px;background:linear-gradient(180deg,var(--white),var(--paper-tint) 60%,var(--white));overflow:hidden;box-shadow:0 2px 8px rgba(0,0,0,.18)}
.page--one{left:26px}.page--two{left:412px}.page--three{left:799px}
.abs{position:absolute}
/* header */
.masthead{left:0;top:0;width:100%;height:44px;background:var(--white)}
.brand{left:20px;top:14px;display:flex;align-items:center;gap:4px;font-size:13px;font-weight:400;color:var(--ink);letter-spacing:-.2px}
.brand-mark{width:14px;height:14px;background:var(--red)}
.contact-top{right:18px;top:12px;font-size:7px;font-weight:700;color:var(--red);line-height:10px}
.contact-top div{display:flex;align-items:center;gap:3px}
.contact-top svg{width:6px;height:6px;fill:var(--ink)}
/* red title band */
.title-band{left:0;top:44px;width:100%;height:30px;background:var(--red);color:var(--white);font-size:12.5px;font-weight:400;display:flex;align-items:center;justify-content:center}
/* hero page 1 */
.hero{left:0;top:48px;width:100%;height:110px;background:linear-gradient(90deg,#3a3a3a,#6b6b6b 50%,#2e2e2e)}
.hero-title{left:0;top:58px;width:100%;text-align:center;color:var(--white);font-size:15.5px;font-weight:300;line-height:18px}
.pill{left:145px;top:118px;height:11px;padding:0 8px;background:var(--red);color:var(--white);font-size:5px;border-radius:3px;line-height:11px}
.name-band{left:0;top:156px;width:100%;height:24px;background:var(--red);color:var(--white);font-size:8px;font-weight:700;padding-left:102px;line-height:24px}
.name-band span{font-weight:400;color:#ffd2d4}
.portrait{border-radius:50%;background:radial-gradient(circle at 50% 40%,#9a9a9a,#4a4a4a);border:3px solid var(--white);box-shadow:0 0 0 1px var(--grey)}
.portrait--lead{left:22px;top:114px;width:64px;height:64px}
.portrait--quote{left:18px;top:122px;width:44px;height:44px}
.lead-head{left:20px;top:190px;width:331px;text-align:center;font-size:9.5px;font-weight:700;color:var(--black);line-height:12px}
.lead-text{left:50px;top:222px;width:271px;text-align:center;font-size:5.4px;line-height:7px}
.dark-band{left:0;width:100%;background:var(--band);color:var(--white)}
.why{top:252px;height:64px}
.why h3{font-size:9px;font-weight:300;text-align:center;margin-top:8px}
.why p{font-size:4.4px;color:#bdbdbd;text-align:center;line-height:5.8px;padding:5px 24px 0}
.red-head{font-size:10px;font-weight:700;color:var(--red);line-height:12px}
.six-head{left:12px;top:326px}
.ticks{left:12px;top:346px;width:350px;list-style:none;font-size:4.6px;line-height:5.8px}
.ticks li{display:flex;gap:4px;margin-bottom:4.4px}
.ticks svg{flex:none;width:5px;height:5px;margin-top:.5px}
/* footer */
.footer{left:0;bottom:0;width:100%;height:22px;background:var(--red);color:var(--white);display:flex;align-items:center;padding-left:12px;gap:12px;font-size:6.8px;font-weight:700}
.footer .cta{font-size:8.5px;font-weight:900}
.footer span{display:flex;align-items:center;gap:3px}
.footer svg{width:6px;height:6px;fill:var(--white)}
/* page 2 */
.section-head{left:0;width:100%;text-align:center;font-size:9px;font-weight:700;color:var(--black)}
.rule{left:160px;width:50px;height:1.5px;background:var(--red)}
.body-copy{font-size:5.2px;line-height:6.8px}
.benefit{left:20px;top:130px;width:331px}
.benefit p{margin-bottom:5px}
.media{top:214px;height:94px;text-align:center}
.media h3{font-size:10px;font-weight:300;margin-top:10px}
.media p{font-size:4.8px;color:#cfcfcf;margin-top:3px}
.outlets{left:22px;top:39px;width:327px;display:flex;justify-content:space-between}
.outlet{width:42px;height:42px;border-radius:50%;background:var(--white)}
.outlet:first-child{background:var(--red)}
.outlet:nth-child(2){background:#1e4a8f}
.outlet:nth-child(4){background:#2b6cb0}
.three-head{left:20px;top:328px;width:200px}
.photo{background:linear-gradient(135deg,#c9c3bb,#8d8077 55%,#5b534e)}
.photo--team{left:230px;top:332px;width:120px;height:128px}
.three-text{left:20px;top:366px;width:200px;font-size:4.7px;line-height:6px}
.three-text .ticks{position:static;width:auto;font-size:4.7px;line-height:6px;margin-top:4px}
.note{font-size:3.8px;margin-top:2px}
/* page 3 */
.testi-head{left:0;top:96px;width:100%;text-align:center;font-size:8.8px;font-weight:700;color:var(--black)}
.quote-lead{left:72px;top:128px;width:282px;font-size:5.2px;line-height:6.8px}
.signature{color:var(--red);font-weight:700;margin-top:4px}
.fc-band{top:208px;height:30px;font-size:6.6px;color:#cfcfcf;text-align:center;line-height:8.5px;padding-top:6px}
.quotes{left:20px;top:252px;width:331px;font-size:5.2px;line-height:6.6px}
.quotes p{margin-bottom:5px}
.sign-block{left:20px;top:344px;font-size:5.2px;line-height:6.6px;color:var(--red);font-weight:700}
.button{left:222px;top:344px;width:126px;height:18px;background:var(--red);color:var(--white);border-radius:3px;font-size:6px;font-weight:700;display:flex;align-items:center;justify-content:center}
.divider{left:20px;top:382px;width:331px;height:1px;background:#d6d6d6}
.book-head{left:20px;top:398px;width:140px;font-size:10px}
.photo--room{left:174px;top:398px;width:174px;height:84px;background:linear-gradient(120deg,#dfe2e4,#8f959a 60%,#4f5458)}
.book-contact{left:20px;top:452px;font-size:5.2px;line-height:6.8px;color:var(--black)}
</style>
</head>
<body>

<svg width="0" height="0" style="position:absolute">
  <defs>
    <symbol id="i-phone" viewBox="0 0 10 10"><path d="M2 0h2l1 3-1.5 1a6 6 0 0 0 2.5 2.5L7 5l3 1v2a2 2 0 0 1-2 2A8 8 0 0 1 0 2a2 2 0 0 1 2-2z"/></symbol>
    <symbol id="i-mail" viewBox="0 0 10 8"><path d="M0 0h10v8H0z M0 0l5 4 5-4" fill="none" stroke="currentColor"/><rect width="10" height="8"/><path d="M0 0l5 4 5-4" stroke="#ec1f27" fill="none"/></symbol>
    <symbol id="i-web" viewBox="0 0 10 10"><circle cx="5" cy="5" r="5"/><circle cx="2.5" cy="5" r=".8" fill="#ec1f27"/><circle cx="5" cy="5" r=".8" fill="#ec1f27"/><circle cx="7.5" cy="5" r=".8" fill="#ec1f27"/></symbol>
    <symbol id="i-tick" viewBox="0 0 10 10"><rect x=".5" y=".5" width="9" height="9" fill="none" stroke="#ec1f27"/><path d="M2 5l2.2 2.2L8.5 2.5" fill="none" stroke="#ec1f27" stroke-width="1.4"/></symbol>
  </defs>
</svg>

<!-- PAGE ONE -->
<section class="page page--one">
  <header class="abs masthead">
    <div class="abs brand"><span class="brand-mark"></span>bargainmentor</div>
    <div class="abs contact-top">
      <div><svg><use href="#i-phone"/></svg>1-888-555-0142</div>
      <div><svg><use href="#i-mail"/></svg>daniel@whitcombe.net</div>
    </div>
  </header>
  <div class="abs hero" role="img" aria-label="Banner photo of a speaker presenting to a seated audience"></div>
  <h1 class="abs hero-title">Turnkey Solutions to improve<br>Negotiating Skills</h1>
  <div class="abs pill">Tailored Negotiating Skills Training</div>
  <div class="abs name-band">DANIEL R. WHITCOMBE <span>THE BARGAIN MENTOR®</span></div>
  <div class="abs portrait portrait--lead" role="img" aria-label="Headshot of Daniel R. Whitcombe"></div>
  <h2 class="abs lead-head">Meet Bargain Mentor® Daniel R. Whitcombe –<br>The Expert You Need As a Guest on Your Podcast</h2>
  <p class="abs lead-text">Are you looking for a relevant and appealing topic and an engaging subject matter expert who can provide measurable value and life-changing tips to the listeners of your podcast?</p>
  <div class="abs dark-band why">
    <h3>Why Negotiating and Decision Making Should Be Topics on Your Podcast</h3>
    <p>Regardless of your podcast theme – it's important to remember that your listeners are negotiating all the time – in their personal lives, social lives, and especially in their business lives. Negotiating is an essential life skill. Everyone can improve his or her negotiating skills, and Daniel is the expert who can provide the answers your people crave. Your podcast listeners will benefit from Daniel's proven, practical, and relevant negotiating strategies and tips that will improve results and outcomes in all types of personal and business negotiations.</p>
  </div>
  <h2 class="abs red-head six-head">Six Reasons to Book Daniel R. Whitcombe As a Guest on Your Podcast</h2>
  <ul class="abs ticks">
    <li><svg><use href="#i-tick"/></svg>Daniel is a dynamic, thought-provoking, engaging, captivating, and entertaining speaker who will share some great personal stories to help your listeners better understand and relate to the topic of negotiating and decision-making dynamics. He will indeed challenge the "status quo."</li>
    <li><svg><use href="#i-tick"/></svg>Daniel is the founder of bargainmentor.net® and is an internationally recognized expert and highly rated speaker on the topics of negotiating and decision-making dynamics that affect negotiated outcomes. His versatility and commitment to proper preparation will ensure that his content is tailored to address the theme of your podcast and the needs of your listeners.</li>
    <li><svg><use href="#i-tick"/></svg>His five-star-rated presentations and training programs have been delivered around the world to small and medium-sized businesses, Top 500 corporations, and large industry, trade, and peer-to-peer associations such as Young Leaders' Network and Founders' Circle.</li>
    <li><svg><use href="#i-tick"/></svg>Daniel has personally trained over 50,000 people of all experience levels, across multiple industries, in 31 countries how to negotiate more effectively.</li>
    <li><svg><use href="#i-tick"/></svg>With formal training in broadcasting and media arts, Daniel provides 30 years of experience as a professional speaker who can provide your listeners with valuable insights, solutions, and answers to address listeners' challenges and questions.</li>
    <li><svg><use href="#i-tick"/></svg>Daniel is the creator of the best-selling Deal Mastery Audio Kit Learning Program – designed to be an effective all-in-one learning solution that helps people improve their negotiating capabilities and skills. He is also the host of his soon-to-be-launched Podcast – Learn to Bargain.</li>
  </ul>
  <footer class="abs footer">
    <span class="cta">CONTACT WITH US</span>
    <span><svg><use href="#i-mail"/></svg>daniel@whitcombe.net</span>
    <span><svg><use href="#i-phone"/></svg>519-555-0187</span>
    <span><svg><use href="#i-web"/></svg>bargainmentor.net</span>
  </footer>
</section>

<!-- PAGE TWO -->
<section class="page page--two">
  <header class="abs masthead">
    <div class="abs brand"><span class="brand-mark"></span>bargainmentor</div>
    <div class="abs contact-top">
      <div><svg><use href="#i-phone"/></svg>1-888-555-0142</div>
      <div><svg><use href="#i-mail"/></svg>daniel@whitcombe.net</div>
    </div>
  </header>
  <div class="abs title-band">Turnkey Solutions to improve Negotiating Skills</div>
  <h2 class="abs section-head" style="top:95px">How Podcast Listeners Will Benefit</h2>
  <div class="abs rule" style="top:110px"></div>
  <div class="abs body-copy benefit">
    <p>Most people are intimidated by the prospect and process of negotiating – and often view negotiating as an uncomfortable haggling and bargaining process that may involve confrontation, anxiety, and stress. If podcast listeners are like most people – then they probably are concerned about being taken advantage of – or that they are missing out on potential opportunities in their personal, social, and business negotiations.</p>
    <p>To alleviate your listeners' concerns, Daniel will provide them with easy-to-understand negotiating strategies, tactics, phrases, and tips they can immediately apply – the moment the podcast episode ends. Your listeners will feel more confident when they are equipped with the powerful and beneficial strategies and techniques that will help them save/make money and arrive at better outcomes when negotiating with customers, clients, suppliers, contractors, financial institutions, retailers, co-workers, colleagues, and family members.</p>
  </div>
  <div class="abs dark-band media">
    <h3>Daniel R. Whitcombe in the Media</h3>
    <p>Daniel has appeared on radio programs, written articles or contributed to articles for the following media outlets:</p>
    <div class="abs outlets">
      <div class="outlet" role="img" aria-label="Media outlet badge"></div>
      <div class="outlet" role="img" aria-label="Media outlet badge"></div>
      <div class="outlet" role="img" aria-label="Media outlet badge"></div>
      <div class="outlet" role="img" aria-label="Media outlet badge"></div>
      <div class="outlet" role="img" aria-label="Media outlet badge"></div>
    </div>
  </div>
  <h2 class="abs red-head three-head">Three Ways You Can Profit From Booking Daniel R. Whitcombe on Your Podcast</h2>
  <div class="abs photo photo--team" role="img" aria-label="Photo of colleagues reviewing documents around a table"></div>
  <div class="abs three-text">
    <p>Upon mutual agreement, podcast hosts and listeners can have access to the following money-saving and profit-generating opportunities:</p>
    <ul class="ticks">
      <li><svg><use href="#i-tick"/></svg>Podcast hosts will be provided with a specific promotional code to share with your listeners that will entitle them to receive a special one-time discount of $19.95US off the purchase of the MP3 download of the Deal Mastery Audio Kit Learning Program available on my online store. Complete download and purchase instructions will be provided to podcast hosts to publish in your notes and also communicate to your listeners.</li>
      <li><svg><use href="#i-tick"/></svg>Podcast hosts will receive a 10% commission payable on the net sales dollar revenue generated from the sale of MP3 downloads of Daniel's Deal Mastery Audio Kit Learning Program.</li>
      <li><svg><use href="#i-tick"/></svg>Podcast hosts will receive a 10% referral fee for any corporation or association that books Daniel for a presentation, seminar, or learning workshop that directly results from my participation on your podcast.</li>
    </ul>
    <p class="note">Note: Discount and commission payments are subject to agreement to standard terms and conditions.</p>
  </div>
  <footer class="abs footer">
    <span class="cta">CONTACT WITH US</span>
    <span><svg><use href="#i-mail"/></svg>daniel@whitcombe.net</span>
    <span><svg><use href="#i-phone"/></svg>519-555-0187</span>
    <span><svg><use href="#i-web"/></svg>bargainmentor.net</span>
  </footer>
</section>

<!-- PAGE THREE -->
<section class="page page--three">
  <header class="abs masthead">
    <div class="abs brand"><span class="brand-mark"></span>bargainmentor</div>
    <div class="abs contact-top">
      <div><svg><use href="#i-phone"/></svg>1-888-555-0142</div>
      <div><svg><use href="#i-mail"/></svg>daniel@whitcombe.net</div>
    </div>
  </header>
  <div class="abs title-band">Turnkey Solutions to improve Negotiating Skills</div>
  <h2 class="abs testi-head">Testimonials: What Some Clients Are Saying About the Bargain Mentor®</h2>
  <div class="abs portrait portrait--quote" role="img" aria-label="Headshot of podcast host Carl Renwick"></div>
  <div class="abs quote-lead">
    <p>"Daniel Whitcombe did a terrific job on my podcast. His negotiating insights and tips were well received by my listeners, and he was an engaging, knowledgeable, and entertaining guest. Given my expertise in real estate, I thought I was a good negotiator – until Daniel taught me a few new strategies and tips during the podcast. I would recommend Daniel to any podcast host – he is a pro and his topics are relevant and can benefit everyone."</p>
    <p class="signature">Carl Renwick, Podcast Host<br>Property Builders Podcast, Austin, Texas</p>
  </div>
  <div class="abs dark-band fc-band">Below is a partial listing of testimonials from attendees at a Founders' Circle<br>(FC) event provided by Liam Dorsett, Chapter Learning Chair:</div>
  <div class="abs quotes">
    <p>"A very engaging, entertaining, and inspirational speaker who provided very useful information, strategies, and tips to apply to all my future negotiations."</p>
    <p>"Thank you to FC Western New York for booking this speaker! I learned some things that I can address immediately and a lot material that I need to practice. Great session!"</p>
    <p>"Daniel was an outstanding speaker on the topic of negotiating! He was one of my favorite speakers ever! Daniel was a real 'teacher' versus other typical speakers who spend two hours bragging or promoting their book."</p>
    <p>"Daniel was a very knowledgeable and well-prepared speaker who provided helpful tips and scripts throughout the entire presentation! I would love to learn more from this speaker."</p>
  </div>
  <div class="abs sign-block">Liam Dorsett, CEO and President<br>Harbor Records Group<br>Founders' Circle (FC) Western New York<br>Learning Chair</div>
  <div class="abs button">Read More Testimonials</div>
  <div class="abs divider"></div>
  <h2 class="abs red-head book-head">Book Bargain Mentor® Daniel R. Whitcombe for Your Podcast</h2>
  <div class="abs photo photo--room" role="img" aria-label="Photo of a presenter leading a workshop in a meeting room"></div>
  <div class="abs book-contact">
    E-mail: daniel@whitcombe.net<br>
    Phone: 519-555-0187<br>
    ProLink Profile: prolink.example/in/danielwhitcombe<br>
    Website: bargainmentor.net
  </div>
  <footer class="abs footer">
    <span class="cta">CONTACT WITH US</span>
    <span><svg><use href="#i-mail"/></svg>daniel@whitcombe.net</span>
    <span><svg><use href="#i-phone"/></svg>519-555-0187</span>
    <span><svg><use href="#i-web"/></svg>bargainmentor.net</span>
  </footer>
</section>

</body>
</html>
```